Gains Beyond the Lantern Gate - book cover design

I need a cover designed for a new book (paperback and eBook).
The title is: “Gains Beyond the Lantern Gate” with the subtitle: “The only book you need to start investing profitably in Chinese stocks”. It is from the first time author :“Teemu Harkala“.
The following text should also be visible in the front cover: “From the founder of OrientWagerly.com” or "Founder of OrientWagerly.com".
The publisher’s logo, should also be visible somewhere on the cover (front, back or spine). The logo, along with source files are here: http://filevault.example/k7Tq2Lp
The book/paperback cover dimensions are: 5.06 x 7.81 inches (12.9 x 19.8 centimeters). Here are the book-cover templates recommended by Bookdale for a book of this size:
http://filevault.example/z3Wm9Xa (.indd)
http://filevault.example/r8Nd4Fu (.pdf)
Below is a description of the book. I don't have a specific idea or vision in mind for the cover. I'd like to see what designs and ideas ArtHuddle designers come up with.
Color red is usually associated with China, but I don’t want the book to be red. Instead the background color could be one of the publisher’s brand colors (#88C198, #017487). However I’ll leave you the designers freedom to propose any colors and combinations.
This is not an entry level book, but a very advanced level investment strategy book for international investors. It explains with concrete examples how non-Chinese citizens can best benefit from China’s economic miracle by picking the best Chinese growth stocks from New York, Hong Kong and Singapore stock exchanges.
The book cover should not have dollar signs promising easy and fast money (because easy and fast money doesn’t exist). What the book promises is a very advanced level China investing strategy, which will considerably improve international investors’ odds for big profits in the longer term.
The big investment themes in the book are China’s consumer sector and service industries.
The book cover should have some kind of reference/association to Investing and China.
The design needs to work and be effective at both a large book cover size and a small thumbnail-sized image - the way that many people browse book covers on Bookdale and other websites. Therefore, a design that relies on really small details probably won't translate at the smaller image sizes that book covers are displayed online.
Target Market(s)
International investors (~50% from western countries, 30% from Singapore/Hong Kong, Malaysia)
Industry/Entity Type
Investment
Font styles to use
Other font styles liked:
- EB Garamond, Grimson text or some other beautiful book font
Look and feel
Each slider illustrates characteristics of the customer's brand and the style your logo design should communicate.

```html
<!DOCTYPE html>
<html lang="en">
<head>
<meta charset="utf-8">
<title>Gains Beyond the Lantern Gate — Teemu Harkala</title>
<link rel="stylesheet" href="https://fonts.googleapis.com/css2?family=Cinzel:wght@400&family=Roboto+Condensed:wght@700&display=swap">
<style>
  :root {
    --teal-light: #1f8e9c;
    --teal-mid: #0c6f7e;
    --teal-dark: #074f5b;
    --ink-light: #ffffff;
    --bull-red: #c4120c;
    --bull-deep: #7a0804;
    --star-gold: #e8d27a;
  }
  * { margin: 0; padding: 0; box-sizing: border-box; }
  html, body { width: 800px; height: 1200px; overflow: hidden; background: var(--teal-dark); }
  .cover {
    position: relative;
    width: 800px;
    height: 1200px;
    overflow: hidden;
    background: radial-gradient(ellipse 75% 55% at 50% 62%, var(--teal-light) 0%, var(--teal-mid) 55%, var(--teal-dark) 100%);
    color: var(--ink-light);
    text-align: center;
  }
  .title {
    position: absolute;
    top: 40px;
    left: 0;
    width: 100%;
    font-family: 'Cinzel', 'Times New Roman', serif;
    font-weight: 400;
  }
  .title-line {
    display: block;
    font-size: 64px;
    line-height: 78px;
    letter-spacing: 2px;
  }
  .title-key {
    display: block;
    margin-top: 6px;
    font-size: 140px;
    line-height: 140px;
    letter-spacing: 26px;
    padding-left: 26px;
  }
  .subtitle {
    position: absolute;
    top: 358px;
    left: 0;
    width: 100%;
    font-family: 'Roboto Condensed', 'Arial Narrow', sans-serif;
    font-weight: 700;
    font-size: 26px;
    line-height: 40px;
    letter-spacing: 2.5px;
    text-transform: uppercase;
  }
  .hero-art {
    position: absolute;
    left: 60px;
    top: 450px;
    width: 650px;
    height: 610px;
    background:
      radial-gradient(ellipse 42% 38% at 52% 45%, var(--bull-red) 0%, var(--bull-red) 45%, rgba(196,18,12,0.55) 70%, rgba(196,18,12,0) 100%),
      radial-gradient(ellipse 20% 14% at 40% 52%, rgba(232,210,122,0.45) 0%, rgba(232,210,122,0) 100%);
    border-radius: 50%;
  }
  .founder {
    position: absolute;
    top: 1072px;
    left: 0;
    width: 100%;
    font-family: 'Cinzel', 'Times New Roman', serif;
    font-size: 24px;
    letter-spacing: 0.5px;
  }
  .author {
    position: absolute;
    top: 1118px;
    left: 0;
    width: 100%;
    font-family: 'Roboto Condensed', 'Arial Narrow', sans-serif;
    font-weight: 700;
    font-size: 44px;
    letter-spacing: 3px;
    text-transform: uppercase;
  }
</style>
</head>
<body>
  <main class="cover">
    <h1 class="title">
      <span class="title-line">GAINS BEYOND</span>
      <span class="title-line">THE LANTERN</span>
      <span class="title-key">GATE</span>
    </h1>
    <p class="subtitle">The only book you need to start investing<br>profitably in Chinese stocks</p>
    <div class="hero-art" role="img" aria-label="Glossy red bull sculpture decorated with gold stars, standing in three-quarter view"></div>
    <p class="founder">From the founder of OrientWagerly.com</p>
    <p class="author">Teemu Harkala</p>
  </main>
</body>
</html>
```